Capability Statement for Consulting firm to effectively market skills to Government buyers and pr...

We need a ONE PAGE capability statement document that is visually interesting and has similar design/graphic elements to my logo and website. A Capability Statement should also show a firm's logo and other branding elements for recognition and be free of long paragraphs, instead, using short sentences and bulleted lists for quick visual scanning.<br/>The five key areas included in a successful Capability Statement are:<br/>1. Core competencies / capabilities<br/>2. Differentiators / including facilities and equipment<br/>3. Past performance<br/>4. Corporate data including industry codes<br/>5. Contact information<br/>The five key areas included in a successful Capability Statement are:<br/>1. Core competencies / capabilities<br/>2. Differentiators / including facilities and equipment<br/>3. Past performance<br/>4. Corporate data including industry codes<br/>5. Contact information<br/>When composing a Capability Statement, use the following section labels: Core Competencies,<br/>Past Performance, and Differentiators. These are the key elements that government buyers are<br/>looking for so that they can make a speedy decision.<br/>1. Core Competencies<br/>These are short introduction statements relating the company's core competencies to the agency's<br/>specific needs followed by key-word heavy bullet points. This is NOT everything a firm is able<br/>to do, but the core expertise of a firm, specifically related to the agency this Capability Statement<br/>is written for, its mission and identified opportunities.<br/>2. Differentiators<br/>Doing business with the government is highly competitive. Contractors have the burden of<br/>dealing with this competitive market and rising above the other contractors. Many companies<br/>who are trying to increase sales to the government market do not have a clear value statement<br/>detailing what makes them different from their competitors. A succinct, clear statement that<br/>relates to the specific needs of the agency is what will help the procurement and purchasing staff,<br/>the program managers and end users understand why they should pick your firm over other<br/>competitors.<br/>Sample Differentiator Questions:<br/>How is your company best suited for the needs of this agency? What is it about your services that<br/>make you stand out from the rest? What is it about your people that give you the advantage over<br/>your competitors? Why are your products better solutions than the others that are available?<br/>If these benefits cannot be clearly communicated, it is impossible for a decision-maker to make a<br/>clear recommendation for your company over one of your competitors. Many companies fail to<br/>take this critical step. And they wonder why they are missing out on contracts.<br/>3. Past Performance<br/>Begin by listing past customers for whom your business has done similar work. Prioritize<br/>starting with related agency, to all federal to other government, to commercial contracts. If the<br/>past projects do not relate to the targeted agency's needs, do not list it.<br/>Tip: Ideally, include specific contact information for immediate references. Include<br/>name, title, email and phone. Use this information when meeting with decision-makers.<br/>Leave this information off the Capability Statement when you are sending the PDF as an<br/>initial outreach effort or leaving as a handout at conferences.<br/>4. Company Data<br/>Include one or two short sentences with a company description detailing pertinent history.<br/>Include the size of your firm, your revenue, the number of employees you have, and the typical<br/>geographic area you serve.<br/>Show contact information, including web site and a specific person's name, email and phone<br/>number, on each side or page of the document.<br/>If your firm has won any awards, received accolades or has notable accomplishments relating to<br/>that agency, list them only if you have space.<br/>Using this information will help in creating a Powerful Capability Statement and open doors to<br/>contracting opportunities in the federal government. This document is the key to building<br/>relationship with important decision-makers in government contracting, providing them with a<br/>concise description of the goods and services your business can provide, and a consistent<br/>reminder of your firm.<br/><br/>Logo must be prominently on top of page<br/><br/>Should be ONE PAGE

Target Market(s)

Government buyers and Prime Contractors

Other font styles liked:
• Be Creative

Colors

Designer to choose colors to be used in the design.

Requirements
Must have
• Be ONE PAGE-BE consistent with branding elements of my webpage
• all of the data and elements provided on the MS Word document
• I must be able to edit the document as needed
• My logo is in the MS word document
Nice to have
• visually compelling document that will attract buyers and concisely present my capabilities.
• Modern and chic
• Girls should want to hang on their and guys should want to emulate
Should not have
• Not more than one page
• copy of other business
• boring and dull

```html
<!DOCTYPE html>
<html lang="en">
<head>
<meta charset="utf-8">
<title>Harrier Project Consultants – Capability Statement</title>
<link href="https://fonts.googleapis.com/css2?family=Montserrat:wght@400;500;600;700;800&display=swap" rel="stylesheet">
<style>
:root{
  --backdrop:#d7d7d7;
  --paper:#ffffff;
  --navy:#1d2635;
  --navy-soft:#2b3647;
  --orange:#f7941d;
  --orange-deep:#e9801a;
  --grey-head:#8a8a8a;
  --ink:#3a3a3a;
  --footer:#3f3f40;
  --white:#ffffff;
}
*{margin:0;padding:0;box-sizing:border-box}
html,body{width:703px;height:1200px;overflow:hidden}
body{background:var(--backdrop);font-family:"Montserrat",Arial,sans-serif;color:var(--ink);position:relative}
.statement{position:absolute;left:6px;top:112px;width:690px;height:975px;background:var(--paper);box-shadow:0 6px 18px rgba(0,0,0,.28);overflow:hidden}

/* header */
.hero{position:absolute;left:0;top:0;width:690px;height:338px;background:linear-gradient(180deg,#1c2433 0%,#283242 70%,#3a3834 100%)}
.hero-skyline{position:absolute;left:0;top:0;width:690px;height:338px}
.brand{position:absolute;left:45px;top:96px;color:var(--white);font-weight:600;font-size:13px;letter-spacing:2px;line-height:1.35;text-transform:uppercase}
.brand-mark{display:block;width:14px;height:14px;border-radius:50%;background:var(--white);margin-bottom:10px}
.tagline{position:absolute;left:45px;top:183px;line-height:1.08}
.tagline .lead{display:block;color:var(--orange);font-weight:500;font-size:20.5px}
.tagline .strong{display:block;color:var(--white);font-weight:800;font-size:26px;margin-top:2px}

/* columns */
.col{position:absolute;top:362px}
.col-left{left:45px;width:260px}
.col-right{left:378px;width:272px}
.section-title{font-size:16.5px;font-weight:700;color:var(--grey-head);text-transform:uppercase;line-height:1.1;margin-bottom:10px}
.section-title span{color:var(--orange)}
.section-title.all-orange{color:var(--orange)}
p.copy{font-size:8.3px;line-height:1.38;text-align:justify;margin-bottom:6px}
.ticks{list-style:none}
.ticks li{position:relative;padding-left:20px;font-size:8.3px;line-height:1.38;margin-bottom:7px}
.ticks li svg{position:absolute;left:0;top:1px;width:11px;height:11px}
.ticks .hl{color:var(--orange)}
.ticks.tight li{margin-bottom:3px}
.gap{height:14px}
.diffs{list-style:none;margin-bottom:14px}
.diffs li{display:flex;align-items:center;gap:14px;font-size:8.3px;font-weight:600;line-height:1.35;margin-bottom:7px;min-height:20px}
.diffs svg{flex:0 0 20px;width:20px;height:20px}

/* footer */
.contact-bar{position:absolute;left:0;bottom:0;width:690px;height:55px}
.contact-bar svg.band{position:absolute;left:0;top:0}
.contact-name{position:absolute;left:45px;top:14px;color:var(--orange);font-weight:600;font-size:15.5px;line-height:1}
.contact-role{position:absolute;left:45px;top:32px;color:var(--white);font-size:7px}
.contact-mid{position:absolute;left:199px;top:16px;color:var(--white);font-size:8.3px;line-height:1.6}
.contact-mid .label{color:var(--orange)}
.contact-mid b{font-weight:700;margin-left:4px}
.contact-right{position:absolute;left:378px;top:16px;color:var(--white);font-size:7.6px;line-height:1.75}
.row{display:flex;align-items:center;gap:6px}
.row svg{width:8px;height:8px;flex:0 0 8px}
.social{position:absolute;right:29px;top:23px;display:flex;gap:3px}
.social span{width:11px;height:11px;background:#3d6ad6;display:block}
.social span+span{background:#2aa3ef}
</style>
</head>
<body>
<main class="statement">

  <header class="hero">
    <svg class="hero-skyline" viewBox="0 0 690 338" role="img" aria-label="Photograph of a downtown city skyline at dusk with glass towers">
      <defs>
        <linearGradient id="skyFill" x1="0" y1="0" x2="0" y2="1">
          <stop offset="0" stop-color="#aebfd2"/>
          <stop offset=".45" stop-color="#7d8c9c"/>
          <stop offset=".75" stop-color="#6b5a4a"/>
          <stop offset="1" stop-color="#8a5a35"/>
        </linearGradient>
        <linearGradient id="warmGlow" x1="0" y1="0" x2="0" y2="1">
          <stop offset="0" stop-color="#f7941d" stop-opacity=".55"/>
          <stop offset="1" stop-color="#f7941d" stop-opacity=".9"/>
        </linearGradient>
      </defs>
      <polygon points="494,0 690,0 690,338 330,338" fill="url(#skyFill)"/>
      <polygon points="376,226 433,338 330,338" fill="url(#warmGlow)"/>
    </svg>
    <div class="brand"><span class="brand-mark"></span>Harrier<br>Project Consultants</div>
    <h1 class="tagline">
      <span class="lead">WE UNCOVER &amp; IMPLEMENT</span>
      <span class="lead">THE RIGHT SOLUTION</span>
      <span class="strong">AT THE RIGHT TIME</span>
      <span class="strong">IN THE RIGHT WAY</span>
    </h1>
  </header>

  <section class="col col-left">
    <h2 class="section-title"><span>Core</span> Competencies</h2>
    <p class="copy">Harrier Project Consultants specializes in custom-designed business strategy and project management solutions. We apply Project Management Standards Board (PMSB) principles to offer technically and commercially sound solutions for government agencies, manufacturing/industrial facilities, power generation plants, water treatment, and commercial strategy.</p>
    <div class="gap"></div>
    <ul class="ticks">
      <li><svg viewBox="0 0 12 12"><circle cx="6" cy="6" r="5" fill="none" stroke="#3a3a3a" stroke-width="1.2"/><path d="M3.5 6l2 2 4-4.5" fill="none" stroke="#3a3a3a" stroke-width="1.4"/></svg><span class="hl">Photovoltaic Application Solutions:</span> expertise in technical design, procurement, and construction to deliver all phases of solar farm construction.</li>
      <li><svg viewBox="0 0 12 12"><circle cx="6" cy="6" r="5" fill="none" stroke="#3a3a3a" stroke-width="1.2"/><path d="M3.5 6l2 2 4-4.5" fill="none" stroke="#3a3a3a" stroke-width="1.4"/></svg><span class="hl">Project Management Expertise:</span> reduce costs, manage risk, and optimize safety.</li>
      <li><svg viewBox="0 0 12 12"><circle cx="6" cy="6" r="5" fill="none" stroke="#3a3a3a" stroke-width="1.2"/><path d="M3.5 6l2 2 4-4.5" fill="none" stroke="#3a3a3a" stroke-width="1.4"/></svg><span class="hl">International Experience and Support:</span> resolve complex problems utilizing our global project experience and resources</li>
      <li><svg viewBox="0 0 12 12"><circle cx="6" cy="6" r="5" fill="none" stroke="#3a3a3a" stroke-width="1.2"/><path d="M3.5 6l2 2 4-4.5" fill="none" stroke="#3a3a3a" stroke-width="1.4"/></svg><span class="hl">Commercial Strategy:</span> operate safer and more cost effectively to maximize your profits</li>
    </ul>
    <div class="gap"></div>
    <h2 class="section-title"><span>Past</span> Performance</h2>
    <ul class="ticks">
      <li><svg viewBox="0 0 12 12"><circle cx="6" cy="6" r="5" fill="none" stroke="#3a3a3a" stroke-width="1.2"/><path d="M3.5 6l2 2 4-4.5" fill="none" stroke="#3a3a3a" stroke-width="1.4"/></svg><span class="hl">Solvera</span> - Mesa Verde Generating Station. We provided engineering, 3D modelling, and engineered pipe supports for a $2 Billion 280 MW solar facility, which was the largest parabolic trough plant in the world. Our engineered pipe supports reduced downtime and reduced maintenance costs as an employee of Forge Industrial.</li>
      <li><svg viewBox="0 0 12 12"><circle cx="6" cy="6" r="5" fill="none" stroke="#3a3a3a" stroke-width="1.2"/><path d="M3.5 6l2 2 4-4.5" fill="none" stroke="#3a3a3a" stroke-width="1.4"/></svg><span class="hl">Al Noor Group</span>- Saudi Arabia Designed, manufactured, and commissioned API 675 compliant chemical injection metering skids that reduced costs via precise chemical dosing for multi-million-dollar industrial water treatment project as an employee of Hydrix corporation.</li>
      <li><svg viewBox="0 0 12 12"><circle cx="6" cy="6" r="5" fill="none" stroke="#3a3a3a" stroke-width="1.2"/><path d="M3.5 6l2 2 4-4.5" fill="none" stroke="#3a3a3a" stroke-width="1.4"/></svg><span class="hl">Petrocor</span>- Baytown and Beaumont Designed, manufactured, and project managed ASME B31.1 compliant custom engineered pipe support systems as an employee of Forge Industrial.</li>
    </ul>
  </section>

  <section class="col col-right">
    <h2 class="section-title all-orange">Differentiators</h2>
    <ul class="diffs">
      <li><svg viewBox="0 0 20 20"><circle cx="10" cy="10" r="9" fill="none" stroke="#f7941d" stroke-width="1.3"/><circle cx="10" cy="10" r="4.5" fill="none" stroke="#f7941d" stroke-width="1.2"/><path d="M10 7.5V10h2" fill="none" stroke="#f7941d" stroke-width="1.1"/></svg>24 Hour Commercial Quote Delivery Available</li>
      <li><svg viewBox="0 0 20 20"><circle cx="10" cy="10" r="9" fill="none" stroke="#f7941d" stroke-width="1.3"/><rect x="5.5" y="7" width="9" height="6" fill="#f7941d"/></svg>Involved with first U.S. solar plant with molten salt thermal energy storage</li>
      <li><svg viewBox="0 0 20 20"><circle cx="10" cy="10" r="9" fill="none" stroke="#f7941d" stroke-width="1.3"/><rect x="6" y="10" width="2" height="4" fill="#f7941d"/><rect x="9" y="7.5" width="2" height="6.5" fill="#f7941d"/><rect x="12" y="5.5" width="2" height="8.5" fill="#f7941d"/></svg>Experienced in waste water, industrial, and municipal water treatment</li>
      <li><svg viewBox="0 0 20 20"><circle cx="10" cy="10" r="9" fill="none" stroke="#3a3a3a" stroke-width="1.2"/><path d="M13 6H7l3.5 4L7 14h6" fill="none" stroke="#3a3a3a" stroke-width="1.1"/></svg>Lean Six Sigma capabilities</li>
    </ul>
    <h2 class="section-title"><span>Company</span> Data</h2>
    <p class="copy">Harrier Project Consultants was formed with the intent of optimizing operations, streamlining project management, and maximizing value creation to best help public and private sector clients turn areas of stagnation into growth.</p>
    <p class="copy">This ethos continues to lie at the core of our firm.</p>
    <p class="copy">We are the consulting firm recognized for asking thorough questions, actively listening, and working relentlessly until the goals are achieved. We are fact-driven and action-oriented. We move our clients forward, to where they need to be.</p>
    <div class="gap" style="height:8px"></div>
    <h2 class="section-title" style="line-height:1.15"><span>List of Specific Pertinent<br>Codes</span> and Data</h2>
    <ul class="ticks tight">
      <li><svg viewBox="0 0 12 12"><circle cx="6" cy="6" r="5" fill="none" stroke="#3a3a3a" stroke-width="1.2"/><path d="M3.5 6l2 2 4-4.5" fill="none" stroke="#3a3a3a" stroke-width="1.4"/></svg>Harrier Project Consultants</li>
      <li><svg viewBox="0 0 12 12"><circle cx="6" cy="6" r="5" fill="none" stroke="#3a3a3a" stroke-width="1.2"/><path d="M3.5 6l2 2 4-4.5" fill="none" stroke="#3a3a3a" stroke-width="1.4"/></svg>DUNS # holder</li>
      <li><svg viewBox="0 0 12 12"><circle cx="6" cy="6" r="5" fill="none" stroke="#3a3a3a" stroke-width="1.2"/><path d="M3.5 6l2 2 4-4.5" fill="none" stroke="#3a3a3a" stroke-width="1.4"/></svg>CAGE Code holder</li>
      <li><svg viewBox="0 0 12 12"><circle cx="6" cy="6" r="5" fill="none" stroke="#3a3a3a" stroke-width="1.2"/><path d="M3.5 6l2 2 4-4.5" fill="none" stroke="#3a3a3a" stroke-width="1.4"/></svg><span class="hl">NAICS Codes:</span> 541611, 221114, 237130, 238160, 238210, 611430, 611699, 541613, 541614, 541612, 541810, 541990</li>
      <li style="margin-top:6px"><svg viewBox="0 0 12 12"><circle cx="6" cy="6" r="5" fill="none" stroke="#3a3a3a" stroke-width="1.2"/><path d="M3.5 6l2 2 4-4.5" fill="none" stroke="#3a3a3a" stroke-width="1.4"/></svg><span class="hl">NIGP Codes:</span> 918-49, 962-58, 918-79, 918-58, 925-53, 918-42, 915-22, 961-56, 958-77, 918-79, 918-76, 918-38, 915-01, 918-07, 209-69, 208-68, 918-35, 918-20, 918-06</li>
      <li style="margin-top:6px"><svg viewBox="0 0 12 12"><circle cx="6" cy="6" r="5" fill="none" stroke="#3a3a3a" stroke-width="1.2"/><path d="M3.5 6l2 2 4-4.5" fill="none" stroke="#3a3a3a" stroke-width="1.4"/></svg>Accept Credit Cards</li>
      <li style="margin-top:4px"><svg viewBox="0 0 12 12"><circle cx="6" cy="6" r="5" fill="none" stroke="#3a3a3a" stroke-width="1.2"/><path d="M3.5 6l2 2 4-4.5" fill="none" stroke="#3a3a3a" stroke-width="1.4"/></svg>Socio-economic status holder</li>
    </ul>
  </section>

  <footer class="contact-bar">
    <svg class="band" width="690" height="55" viewBox="0 0 690 55" aria-hidden="true">
      <polygon points="0,0 564,0 614,55 0,55" fill="#3f3f40"/>
      <polygon points="590,24 603,24 631,55 618,55" fill="#f7941d"/>
      <polygon points="607,24 614,24 642,55 635,55" fill="#f7941d"/>
    </svg>
    <div class="contact-name">Daniel Carver</div>
    <div class="contact-role">VP of Project Management</div>
    <div class="contact-mid">
      <div><span class="label">CALL US NOW:</span><b>(555) 201 -4380</b></div>
      <div class="row"><svg viewBox="0 0 8 8"><path d="M4 0.5a2.6 2.6 0 0 1 2.6 2.6C6.6 5 4 7.6 4 7.6S1.4 5 1.4 3.1A2.6 2.6 0 0 1 4 .5z" fill="#f7941d"/><circle cx="4" cy="3" r="1" fill="#3f3f40"/></svg>410 Meridian Ave, Suite 900 Houston, TX</div>
    </div>
    <div class="contact-right">
      <div class="row"><svg viewBox="0 0 8 8"><rect x=".5" y="1.5" width="7" height="5" fill="#f7941d"/><path d="M.5 1.5L4 4.5l3.5-3" fill="none" stroke="#3f3f40" stroke-width=".8"/></svg>dcarver@harrierprojects.com</div>
      <div class="row"><svg viewBox="0 0 8 8"><circle cx="4" cy="4" r="3.5" fill="#f7941d"/><path d="M.5 4h7M4 .5c-2 2-2 5 0 7M4 .5c2 2 2 5 0 7" fill="none" stroke="#3f3f40" stroke-width=".6"/></svg>www.harrierprojects.com</div>
    </div>
    <div class="social" aria-hidden="true"><span></span><span></span></div>
  </footer>

</main>
</body>
</html>
```